Enterprise Application UI beautification

We have an enterprise application that is being redesigned. A screenshot from the new UX/UI is provided. The current UI design is OK but we would like it to look better. The key goals of the UI are to look like a premium product (think luxury brand) and for it to be visually very appealing/attractive. When people see the UI we want them to have a significant, positive reaction. They should "ooh" and "ahh". This is a product sold to large enterprises, not consumers. The current UI is a little plain. The colors we want to use are blue, yellow, black, white and gray. We probably don't want different colors but feel free to use any variations within or close to that color scheme that you see fit. Also feel free to modify the spacing, icons, widgets, tables, fonts, etc.

Target Market(s)

Large enterprise customers (Summit 300).

Number of Pages Required

1 page

Font styles to use
Sans Serif

Colors
3277b5

Requirements
Must have
• A premium feel.

```html
<!DOCTYPE html>
<html lang="en">
<head>
<meta charset="utf-8">
<title>Data Sources</title>
<link href="https://fonts.googleapis.com/css2?family=Nunito+Sans:wght@400;600;700&display=swap" rel="stylesheet">
<style>
:root{
  --navy:#0b3a6e;
  --navy-deep:#0a3466;
  --blue:#2b86e6;
  --blue-text:#2a7fd8;
  --ink:#1b3f73;
  --text:#2b2f38;
  --muted:#5c6470;
  --page:#eef1f8;
  --line:#dfe4ee;
  --row-alt:#f5f7fb;
  --white:#ffffff;
  --active:#e3e9f6;
}
*{box-sizing:border-box;margin:0;padding:0}
html,body{width:1200px;height:821px;overflow:hidden}
body{font-family:"Nunito Sans",sans-serif;background:var(--page);position:relative;color:var(--text)}
.sidebar{position:absolute;left:0;top:0;width:80px;height:821px;background:var(--navy)}
.brand{position:absolute;left:0;top:22px;width:80px;text-align:center;color:var(--white);font-weight:700;font-size:13px;letter-spacing:.5px}
.nav-item{position:absolute;left:0;width:80px;height:50px;display:flex;align-items:center;justify-content:center}
.nav-item.active{background:var(--active)}
.topbar{position:absolute;left:80px;top:0;width:1120px;height:61px;background:var(--blue)}
.user-btn{position:absolute;left:943px;top:17px;width:119px;height:28px;border-radius:14px;background:var(--navy-deep);color:var(--white);font-size:12.5px;display:flex;align-items:center;justify-content:center;gap:5px}
.list-panel{position:absolute;left:80px;top:61px;width:280px;height:760px;background:var(--white)}
.list-title{position:absolute;left:27px;top:28px;font-size:16.5px;font-weight:700;color:var(--ink)}
.list-add{position:absolute;left:217px;top:31px;font-size:12px;color:var(--blue-text)}
.search{position:absolute;left:24px;top:60px;width:233px;height:29px;border-radius:15px;background:var(--page);font-size:10.5px;color:var(--text);display:flex;align-items:center;padding-left:15px;gap:5px}
.source{position:absolute;left:0;width:278px;border-bottom:1px solid var(--line);padding-left:30px}
.source .name{font-size:12.5px;color:var(--text);line-height:16px}
.source .kind{font-size:10px;color:var(--blue-text);line-height:13px}
.scrollbar{position:absolute;left:278px;top:112px;width:3px;height:61px;background:var(--navy);border-radius:2px}
.card{position:absolute;left:389px;width:766px;background:var(--white)}
.card-title{position:absolute;left:40px;font-size:16.5px;font-weight:700;color:var(--ink)}
.btn{position:absolute;top:26px;height:24px;border:1px solid #cfd8e6;border-radius:12px;font-size:9px;font-weight:600;color:var(--blue-text);display:flex;align-items:center;justify-content:center;gap:4px}
.lbl{position:absolute;font-size:11.5px;color:var(--text)}
.val{position:absolute;font-size:11.5px;font-weight:700;color:var(--blue-text)}
.section-title{position:absolute;left:36px;top:25px;font-size:16.5px;font-weight:700;color:var(--ink)}
.section-add{position:absolute;left:146px;top:29px;font-size:10.5px;color:var(--blue-text)}
.obj{position:absolute;left:31px;font-size:10.5px;font-weight:700;color:var(--ink);display:flex;align-items:center;gap:6px}
.obj-x{position:absolute;left:272px}
.obj-line{position:absolute;left:29px;width:646px;height:1px;background:var(--line)}
.fields{position:absolute;left:173px;top:61px;font-size:10.5px;font-weight:700;color:var(--ink)}
.fields span{font-weight:400;color:var(--blue-text)}
table.field-table{position:absolute;left:31px;top:84px;width:644px;border-collapse:collapse;border:1px solid var(--blue);font-size:9px}
.field-table th{background:var(--blue);color:var(--white);font-weight:600;height:25px;text-align:left;padding-left:16px;font-size:8.5px}
.field-table td{height:28px;border-right:1px solid var(--line);padding-left:16px;color:var(--muted)}
.field-table tr:nth-child(odd) td{background:var(--row-alt)}
.field-table td:last-child,.field-table th:last-child{border-right:none}
.field-table td.c{padding-left:0;text-align:center}
.chk{display:inline-block;width:15px;height:14px;border:1px solid #9aa4b2;border-radius:1px;background:var(--white);vertical-align:middle}
.icons{display:flex;align-items:center;gap:5px}
.glyph-a{font-weight:700;font-size:12px;color:var(--blue-text);line-height:1}
.glyph-a.off{color:#b9c0cc}
</style>
</head>
<body>
<aside class="sidebar">
  <div class="brand">Cloudforge</div>
  <div class="nav-item" style="top:78px"><svg width="36" height="24" viewBox="0 0 36 24" fill="none" stroke="#fff" stroke-width="1.6"><circle cx="9" cy="8" r="4"/><circle cx="18" cy="7" r="4.5"/><circle cx="27" cy="8" r="4"/><path d="M2 21c0-5 3-7 7-7M34 21c0-5-3-7-7-7M10 22c0-6 4-8 8-8s8 2 8 8z"/></svg></div>
  <div class="nav-item" style="top:130px"><svg width="30" height="30" viewBox="0 0 30 30" fill="none" stroke="#fff" stroke-width="1.6"><path d="M8 16a6 6 0 0 1 1-11 8 8 0 0 1 14 3 5 5 0 0 1 0 10"/><rect x="7" y="14" width="16" height="9" rx="1"/><path d="M4 26h22"/></svg></div>
  <div class="nav-item active" style="top:189px"><svg width="26" height="28" viewBox="0 0 26 28" fill="none" stroke="#1e63b0" stroke-width="1.7"><path d="M8 2h10l5 5v16H8z"/><path d="M4 6v20h14"/><path d="M12 13h7M12 17h7"/></svg></div>
  <div class="nav-item" style="top:246px"><svg width="24" height="28" viewBox="0 0 24 28" fill="none" stroke="#fff" stroke-width="1.6"><path d="M5 2h11l5 5v18H5z"/><path d="M9 10h8M9 14h8M9 18h8"/><circle cx="5" cy="22" r="4" fill="#0b3a6e"/><path d="M3 22l1.5 1.5L7 21"/></svg></div>
  <div class="nav-item" style="top:306px"><svg width="26" height="26" viewBox="0 0 26 26" fill="none" stroke="#fff" stroke-width="1.6"><rect x="2" y="4" width="22" height="20" rx="2"/><path d="M2 9h22M7 1v5M19 1v5"/><path d="M6 13h2M11 13h2M16 13h2M6 17h2M11 17h2M16 17h2M6 21h2M11 21h2M16 21h2"/></svg></div>
  <div class="nav-item" style="top:358px"><svg width="28" height="28" viewBox="0 0 28 28" fill="none" stroke="#fff" stroke-width="1.5"><rect x="10" y="2" width="8" height="5"/><rect x="3" y="12" width="7" height="4"/><rect x="18" y="12" width="7" height="4"/><path d="M14 7v3M6 10h16M6 10v2M22 10v2M14 10v6"/><circle cx="5" cy="23" r="2.5"/><circle cx="14" cy="23" r="2.5"/><circle cx="23" cy="23" r="2.5"/><path d="M6 16v4M14 16v4M22 16v4"/></svg></div>
</aside>

<header class="topbar">
  <div class="user-btn"><svg width="10" height="10" viewBox="0 0 10 10"><circle cx="5" cy="5" r="3.4" fill="none" stroke="#fff" stroke-width="2.2" stroke-dasharray="2 1.3"/><circle cx="5" cy="5" r="1.2" fill="#fff"/></svg>Dana Mercer<svg width="10" height="6" viewBox="0 0 10 6"><path d="M1 1l4 4 4-4" fill="none" stroke="#fff" stroke-width="1.4"/></svg></div>
</header>

<section class="list-panel">
  <div class="list-title">Data Sources</div>
  <div class="list-add">+Add</div>
  <div class="search"><svg width="9" height="9" viewBox="0 0 9 9"><circle cx="3.7" cy="3.7" r="2.8" fill="none" stroke="#1b3f73" stroke-width="1.4"/><path d="M5.8 5.8L8.4 8.4" stroke="#1b3f73" stroke-width="1.5"/></svg>Search</div>
  <div class="source" style="top:115px;height:52px;padding-left:30px"><div class="name">Cloudforge - Sandbox</div><div class="kind">Cloudforge.io</div></div>
  <div class="source" style="top:169px;height:55px"><div class="name">Polar Test 1 (administrator)</div><div class="kind">Cloudforge.io</div></div>
  <div class="source" style="top:225px;height:61px"><div class="name">Polar Test 2 (administrator)</div><div class="kind">PolarSQL</div></div>
  <div class="source" style="top:282px;height:55px"><div class="name">Sadga</div><div class="kind">Cloudforge.io</div></div>
  <div class="source" style="top:339px;height:53px"><div class="name">Cloudforge Test 1 (masterd ev)</div><div class="kind">PolarSQL</div></div>
  <div class="source" style="top:393px;height:55px"><div class="name">CFDC - Field Entry Test</div><div class="kind">Cloudforge.io</div></div>
  <div class="source" style="top:444px;height:52px"><div class="name">CFDC 44</div><div class="kind">Cloudforge.io</div></div>
  <div class="source" style="top:499px;height:55px;padding-left:31px"><div class="name">CFDC 66</div><div class="kind">Cloudforge.io</div></div>
  <div class="scrollbar"></div>
</section>

<section class="card" style="top:90px;height:269px">
  <div class="card-title" style="top:28px">Cloudforge - Sandbox</div>
  <div class="btn" style="left:245px;width:73px"><svg width="11" height="11" viewBox="0 0 11 11" fill="none" stroke="#2a7fd8" stroke-width="1"><path d="M2 1h5l2 2v7H2z"/><path d="M4 5h3M4 7h2"/></svg>Edit</div>
  <div class="btn" style="left:328px;width:73px"><svg width="11" height="11" viewBox="0 0 11 11" fill="none" stroke="#2a7fd8" stroke-width="1"><rect x="3" y="3" width="7" height="7"/><path d="M1 8V1h7"/></svg>Clone</div>
  <div class="btn" style="left:406px;width:73px"><svg width="11" height="11" viewBox="0 0 11 11" fill="none" stroke="#2a7fd8" stroke-width="1"><circle cx="5.5" cy="5.5" r="4.5"/><path d="M3.7 3.7l3.6 3.6M7.3 3.7L3.7 7.3"/></svg>Delete</div>
  <div class="btn" style="left:647px;top:24px;width:106px"><svg width="8" height="11" viewBox="0 0 8 11" fill="none" stroke="#2a7fd8" stroke-width="1"><path d="M5 1L1 6h3l-1 4 4-5H4z"/></svg>Test Connection</div>

  <div class="lbl" style="left:44px;top:88px">Data Source Name</div><div class="val" style="left:180px;top:88px">Cloudforge - Sandbox</div>
  <div class="lbl" style="left:44px;top:118px">Data Source Type</div><div class="val" style="left:180px;top:118px">Application</div>
  <div class="lbl" style="left:44px;top:149px">Status</div><div class="val" style="left:180px;top:149px">Active</div>
  <div class="lbl" style="left:44px;top:179px">Created by</div><div class="val" style="left:180px;top:179px">Hartwells.test</div>
  <div class="lbl" style="left:44px;top:209px">Last updated by</div><div class="val" style="left:180px;top:209px">Hartwells.test</div>

  <div class="lbl" style="left:385px;top:87px">Username</div><div class="val" style="left:520px;top:87px">masterdev@dev.quillstack.net</div>
  <div class="lbl" style="left:385px;top:117px">Security Token</div><div class="val" style="left:520px;top:117px">tadkaji4234ifnndkn3</div>
  <div class="lbl" style="left:385px;top:147px">Enviorment Type</div><div class="val" style="left:520px;top:147px">Production</div>
  <div class="lbl" style="left:385px;top:178px">Connected App</div><div class="val" style="left:520px;top:178px">No</div>
</section>

<section class="card" style="top:374px;height:411px">
  <div class="section-title">Data Objects</div>
  <div class="section-add">+Add</div>

  <div class="obj" style="top:62px;left:31px"><svg width="8" height="5" viewBox="0 0 8 5"><path d="M1 4.5l3-3 3 3" fill="none" stroke="#1b3f73" stroke-width="1.3"/></svg>Account</div>
  <svg class="obj-x" style="top:64px" width="11" height="11" viewBox="0 0 11 11" fill="none" stroke="#2a7fd8" stroke-width="1"><circle cx="5.5" cy="5.5" r="4.8"/><path d="M3.7 3.7l3.6 3.6M7.3 3.7L3.7 7.3"/></svg>
  <div class="fields">Fields <span>+Add</span></div>

  <table class="field-table">
    <colgroup><col style="width:114px"><col style="width:147px"><col style="width:73px"><col style="width:116px"><col style="width:95px"><col></colgroup>
    <thead><tr><th>Field Name</th><th>Data Type</th><th style="padding-left:12px">Primary Key</th><th style="padding-left:23px">Rule Type</th><th style="padding-left:12px">Sensitive Data</th><th style="padding-left:22px">Actions</th></tr></thead>
    <tbody>
      <tr><td>Account description</td><td>Common.Text</td><td class="c"><span class="chk" style="border-color:#2a7fd8;position:relative"><svg width="13" height="12" viewBox="0 0 13 12" style="position:absolute;left:0;top:0"><path d="M3 6l2.5 2.5L10 3" fill="none" stroke="#2a7fd8" stroke-width="1.4"/></svg></span></td>
        <td><div class="icons" style="padding-left:8px"><span class="glyph-a">a</span><svg width="8" height="8" viewBox="0 0 8 8"><circle cx="3.3" cy="3.3" r="2.5" fill="none" stroke="#b9c0cc" stroke-width="1"/><path d="M5 5l2.5 2.5" stroke="#b9c0cc"/></svg><svg width="8" height="8" viewBox="0 0 8 8"><rect x="2.5" y="0.5" width="5" height="5" fill="none" stroke="#2a7fd8"/><rect x="0.5" y="2.5" width="5" height="5" fill="#2a7fd8"/></svg><svg width="9" height="8" viewBox="0 0 9 8"><path d="M1 1v3h7V1M4.5 4v4" fill="none" stroke="#b9c0cc"/></svg><svg width="7" height="7" viewBox="0 0 7 7"><path d="M3.5 0.5l3 3-3 3-3-3z" fill="none" stroke="#b9c0cc"/></svg><svg width="4" height="6" viewBox="0 0 4 6"><path d="M0 0l4 3-4 3z" fill="#b9c0cc"/></svg></div></td>
        <td><div class="icons" style="padding-left:10px;gap:8px"><svg width="11" height="13" viewBox="0 0 11 13"><rect x="0.5" y="1.5" width="10" height="11" rx="1" fill="none" stroke="#9cc2ec"/><rect x="3" y="0.5" width="5" height="2.5" fill="#9cc2ec"/></svg><svg width="14" height="10" viewBox="0 0 14 10"><rect x="0.5" y="0.5" width="13" height="9" rx="1" fill="none" stroke="#9cc2ec"/><rect x="0.5" y="3" width="13" height="2" fill="#9cc2ec"/></svg><svg width="11" height="11" viewBox="0 0 11 11"><circle cx="5.5" cy="3" r="2.7" fill="#9cc2ec"/><path d="M0.5 11c0-4 2-5 5-5s5 1 5 5z" fill="#9cc2ec"/></svg></div></td>
        <td><div class="icons" style="padding-left:22px;gap:6px"><svg width="12" height="12" viewBox="0 0 12 12" fill="none" stroke="#2a7fd8"><path d="M5 2H1v9h9V7"/><path d="M4 8l1-3 5-5 2 2-5 5z"/></svg><svg width="11" height="11" viewBox="0 0 11 11" fill="none" stroke="#1b3f73" stroke-width="1.1"><circle cx="5.5" cy="5.5" r="4.8"/><path d="M3.7 3.7l3.6 3.6M7.3 3.7L3.7 7.3"/></svg></div></td></tr>
      <tr><td>Account Fax</td><td>Address.Address Line 3</td><td class="c"><span class="chk"></span></td>
        <td><div class="icons" style="padding-left:8px"><span class="glyph-a">a</span><svg width="8" height="8" viewBox="0 0 8 8"><circle cx="3.3" cy="3.3" r="2.5" fill="none" stroke="#b9c0cc" stroke-width="1"/><path d="M5 5l2.5 2.5" stroke="#b9c0cc"/></svg><svg width="8" height="8" viewBox="0 0 8 8"><rect x="2.5" y="0.5" width="5" height="5" fill="none" stroke="#2a7fd8"/><rect x="0.5" y="2.5" width="5" height="5" fill="#2a7fd8"/></svg><svg width="9" height="8" viewBox="0 0 9 8"><path d="M1 1v3h7V1M4.5 4v4" fill="none" stroke="#b9c0cc"/></svg><svg width="7" height="7" viewBox="0 0 7 7"><path d="M3.5 0.5l3 3-3 3-3-3z" fill="none" stroke="#b9c0cc"/></svg><svg width="4" height="6" viewBox="0 0 4 6"><path d="M0 0l4 3-4 3z" fill="#b9c0cc"/></svg></div></td>
        <td><div class="icons" style="padding-left:10px;gap:8px"><svg width="11" height="13" viewBox="0 0 11 13"><rect x="0.5" y="1.5" width="10" height="11" rx="1" fill="none" stroke="#9cc2ec"/><rect x="3" y="0.5" width="5" height="2.5" fill="#9cc2ec"/></svg><svg width="14" height="10" viewBox="0 0 14 10"><rect x="0.5" y="0.5" width="13" height="9" rx="1" fill="none" stroke="#9cc2ec"/><rect x="0.5" y="3" width="13" height="2" fill="#9cc2ec"/></svg><svg width="11" height="11" viewBox="0 0 11 11"><circle cx="5.5" cy="3" r="2.7" fill="#9cc2ec"/><path d="M0.5 11c0-4 2-5 5-5s5 1 5 5z" fill="#9cc2ec"/></svg></div></td>
        <td><div class="icons" style="padding-left:22px;gap:6px"><svg width="12" height="12" viewBox="0 0 12 12" fill="none" stroke="#2a7fd8"><path d="M5 2H1v9h9V7"/><path d="M4 8l1-3 5-5 2 2-5 5z"/></svg><svg width="11" height="11" viewBox="0 0 11 11" fill="none" stroke="#1b3f73" stroke-width="1.1"><circle cx="5.5" cy="5.5" r="4.8"/><path d="M3.7 3.7l3.6 3.6M7.3 3.7L3.7 7.3"/></svg></div></td></tr>
      <tr><td>Acccout ID</td><td>Common ID</td><td class="c"><span class="chk"></span></td>
        <td><div class="icons" style="padding-left:8px"><span class="glyph-a">a</span><svg width="8" height="8" viewBox="0 0 8 8"><circle cx="3.3" cy="3.3" r="2.5" fill="none" stroke="#1b3f73" stroke-width="1.3"/><path d="M5 5l2.5 2.5" stroke="#1b3f73" stroke-width="1.3"/></svg><svg width="8" height="8" viewBox="0 0 8 8"><rect x="2.5" y="0.5" width="5" height="5" fill="none" stroke="#b9c0cc"/><rect x="0.5" y="2.5" width="5" height="5" fill="none" stroke="#b9c0cc"/></svg><svg width="9" height="8" viewBox="0 0 9 8"><path d="M1 1v3h7V1M4.5 4v4" fill="none" stroke="#b9c0cc"/></svg><svg width="7" height="7" viewBox="0 0 7 7"><path d="M3.5 0.5l3 3-3 3-3-3z" fill="none" stroke="#b9c0cc"/></svg><svg width="4" height="6" viewBox="0 0 4 6"><path d="M0 0l4 3-4 3z" fill="#b9c0cc"/></svg></div></td>
        <td><div class="icons" style="padding-left:10px;gap:8px"><svg width="11" height="13" viewBox="0 0 11 13"><rect x="0.5" y="1.5" width="10" height="11" rx="1" fill="none" stroke="#9cc2ec"/><rect x="3" y="0.5" width="5" height="2.5" fill="#9cc2ec"/></svg><svg width="14" height="10" viewBox="0 0 14 10"><rect x="0.5" y="0.5" width="13" height="9" rx="1" fill="none" stroke="#9cc2ec"/><rect x="0.5" y="3" width="13" height="2" fill="#9cc2ec"/></svg><svg width="11" height="11" viewBox="0 0 11 11"><circle cx="5.5" cy="3" r="2.7" fill="#9cc2ec"/><path d="M0.5 11c0-4 2-5 5-5s5 1 5 5z" fill="#9cc2ec"/></svg></div></td>
        <td><div class="icons" style="padding-left:22px;gap:6px"><svg width="12" height="12" viewBox="0 0 12 12" fill="none" stroke="#2a7fd8"><path d="M5 2H1v9h9V7"/><path d="M4 8l1-3 5-5 2 2-5 5z"/></svg><svg width="11" height="11" viewBox="0 0 11 11" fill="none" stroke="#1b3f73" stroke-width="1.1"><circle cx="5.5" cy="5.5" r="4.8"/><path d="M3.7 3.7l3.6 3.6M7.3 3.7L3.7 7.3"/></svg></div></td></tr>
      <tr><td>Accout Name</td><td>Address.Address Line 2</td><td class="c"><span class="chk"></span></td>
        <td><div class="icons" style="padding-left:8px"><span class="glyph-a off">a</span><svg width="8" height="8" viewBox="0 0 8 8"><circle cx="3.3" cy="3.3" r="2.5" fill="none" stroke="#b9c0cc" stroke-width="1"/><path d="M5 5l2.5 2.5" stroke="#b9c0cc"/></svg><svg width="8" height="8" viewBox="0 0 8 8"><rect x="2.5" y="0.5" width="5" height="5" fill="none" stroke="#2a7fd8"/><rect x="0.5" y="2.5" width="5" height="5" fill="#2a7fd8"/></svg><svg width="9" height="8" viewBox="0 0 9 8"><path d="M1 1v3h7V1M4.5 4v4" fill="none" stroke="#b9c0cc"/></svg><svg width="7" height="7" viewBox="0 0 7 7"><path d="M3.5 0.5l3 3-3 3-3-3z" fill="none" stroke="#b9c0cc"/></svg><svg width="4" height="6" viewBox="0 0 4 6"><path d="M0 0l4 3-4 3z" fill="#b9c0cc"/></svg></div></td>
        <td><div class="icons" style="padding-left:10px;gap:8px"><svg width="11" height="13" viewBox="0 0 11 13"><rect x="0.5" y="1.5" width="10" height="11" rx="1" fill="none" stroke="#9cc2ec"/><rect x="3" y="0.5" width="5" height="2.5" fill="#9cc2ec"/></svg><svg width="14" height="10" viewBox="0 0 14 10"><rect x="0.5" y="0.5" width="13" height="9" rx="1" fill="none" stroke="#9cc2ec"/><rect x="0.5" y="3" width="13" height="2" fill="#9cc2ec"/></svg><svg width="11" height="11" viewBox="0 0 11 11"><circle cx="5.5" cy="3" r="2.7" fill="#9cc2ec"/><path d="M0.5 11c0-4 2-5 5-5s5 1 5 5z" fill="#9cc2ec"/></svg></div></td>
        <td><div class="icons" style="padding-left:22px;gap:6px"><svg width="12" height="12" viewBox="0 0 12 12" fill="none" stroke="#2a7fd8"><path d="M5 2H1v9h9V7"/><path d="M4 8l1-3 5-5 2 2-5 5z"/></svg><svg width="11" height="11" viewBox="0 0 11 11" fill="none" stroke="#1b3f73" stroke-width="1.1"><circle cx="5.5" cy="5.5" r="4.8"/><path d="M3.7 3.7l3.6 3.6M7.3 3.7L3.7 7.3"/></svg></div></td></tr>
    </tbody>
  </table>

  <div class="obj" style="top:243px"><svg width="8" height="5" viewBox="0 0 8 5"><path d="M1 0.5l3 3 3-3" fill="none" stroke="#1b3f73" stroke-width="1.3"/></svg>Asset</div>
  <svg class="obj-x" style="top:245px" width="11" height="11" viewBox="0 0 11 11" fill="none" stroke="#2a7fd8" stroke-width="1"><circle cx="5.5" cy="5.5" r="4.8"/><path d="M3.7 3.7l3.6 3.6M7.3 3.7L3.7 7.3"/></svg>
  <div class="obj-line" style="top:264px"></div>
  <div class="obj" style="top:273px"><svg width="8" height="5" viewBox="0 0 8 5"><path d="M1 0.5l3 3 3-3" fill="none" stroke="#1b3f73" stroke-width="1.3"/></svg>Asset Relationship</div>
  <svg class="obj-x" style="top:275px" width="11" height="11" viewBox="0 0 11 11" fill="none" stroke="#2a7fd8" stroke-width="1"><circle cx="5.5" cy="5.5" r="4.8"/><path d="M3.7 3.7l3.6 3.6M7.3 3.7L3.7 7.3"/></svg>
  <div class="obj-line" style="top:294px"></div>
  <div class="obj" style="top:303px"><svg width="8" height="5" viewBox="0 0 8 5"><path d="M1 0.5l3 3 3-3" fill="none" stroke="#1b3f73" stroke-width="1.3"/></svg>Asset Token Event</div>
  <svg class="obj-x" style="top:305px" width="11" height="11" viewBox="0 0 11 11" fill="none" stroke="#2a7fd8" stroke-width="1"><circle cx="5.5" cy="5.5" r="4.8"/><path d="M3.7 3.7l3.6 3.6M7.3 3.7L3.7 7.3"/></svg>
  <div class="obj-line" style="top:324px"></div>
  <div class="obj" style="top:333px"><svg width="8" height="5" viewBox="0 0 8 5"><path d="M1 0.5l3 3 3-3" fill="none" stroke="#1b3f73" stroke-width="1.3"/></svg>Case</div>
  <svg class="obj-x" style="top:335px" width="11" height="11" viewBox="0 0 11 11" fill="none" stroke="#2a7fd8" stroke-width="1"><circle cx="5.5" cy="5.5" r="4.8"/><path d="M3.7 3.7l3.6 3.6M7.3 3.7L3.7 7.3"/></svg>
</section>
</body>
</html>
```